Seeking for catalogue design -for Event Mgmt company

Need to be creative and striking and images to be more enhanced.
The items in the catalogue have to be layout well and easy to read.
Cover and background of catalogue needs to be striking but not overpowering the items.
Catologue needs to be able to put up on website and able to read on mobile.
Font used must be easily readable and not too small.

Target Market(s)

Business and Public Sectors

Industry/Entity Type

Event Planning

Colors

Designer to choose colors to be used in the design.

Requirements
Must have
• Not too many colors but must be creative
Nice to have
• See that the images of items in catalogue have better layout
Should not have
• Not to be so messy

```html
<!DOCTYPE html>
<html lang="en">
<head>
<meta charset="utf-8">
<title>Corvane Events – Carnival Game Stalls Catalogue</title>
<link href="https://fonts.googleapis.com/css2?family=Cormorant+Garamond:wght@500;600&family=Montserrat:wght@400;500;700&family=Roboto:wght@400;500;700&display=swap" rel="stylesheet">
<style>
:root{
  --wine:#6c0015;
  --wine-light:#8c0b24;
  --wine-dark:#54000f;
  --paper:#f3f3f3;
  --silver:#c9c9c9;
  --ink:#333;
  --stage:#7b7b7b;
  --white:#fff;
}
*{box-sizing:border-box;margin:0;padding:0}
html,body{width:848px;height:1200px;overflow:hidden}
body{background:var(--stage);position:relative;font-family:"Montserrat",sans-serif;color:var(--ink)}
.spread{position:absolute;left:65px;width:721px;height:510px;display:flex}
.spread--outside{top:74px}
.spread--inside{top:625px}
.page{position:relative;width:50%;height:100%;overflow:hidden}

/* Outside back */
.back{background:linear-gradient(180deg,var(--paper) 0 177px,var(--wine) 177px 486px,#bdbdbd 486px 490px,#fafafa 490px)}
.back__intro{position:absolute;top:0;left:0;right:0;height:177px;background:linear-gradient(160deg,#fff,#ececec)}
.quote-rule{position:absolute;top:54px;height:1px;background:#d3d3d3;width:115px}
.quote-rule--l{left:42px}.quote-rule--r{right:35px}
.quote-mark{position:absolute;top:22px;left:0;right:0;text-align:center;font-family:"Cormorant Garamond",serif;font-size:88px;line-height:88px;color:#c4c4c4;font-weight:600}
.intro-text{position:absolute;top:68px;left:42px;right:35px;font-size:6.6px;line-height:9px;text-align:center;color:#333}
.intro-text p{margin-bottom:8px}
.intro-text p.justify{text-align:justify;text-align-last:center}
.back__contact{position:absolute;top:177px;left:0;right:0;height:309px;text-align:center;color:var(--white)}
.brand-name{font-family:"Cormorant Garamond",serif;font-weight:500;letter-spacing:1px;line-height:1;white-space:nowrap}
.back .brand-name{margin-top:67px;font-size:30px}
.brand-sub{font-family:"Cormorant Garamond",serif;font-size:6.5px;letter-spacing:.5px;white-space:nowrap}
.contact-icons{display:flex;justify-content:center;gap:9px;margin-top:19px}
.contact-icons svg{width:15px;height:15px}
.address{margin-top:9px;font-size:8.4px;line-height:12px}
.web{margin-top:5px;font-size:8.4px;line-height:12px}
.tagline{margin-top:14px;font-size:6.5px}
.social{margin-top:8px;font-size:6.6px;letter-spacing:.6px;display:flex;justify-content:center;align-items:center;gap:5px}
.social .dot{width:9px;height:9px;border:1px solid var(--white);border-radius:50%}

/* Outside cover */
.cover{background:linear-gradient(180deg,var(--wine-light),var(--wine) 60%,var(--wine-dark) 486px,#bdbdbd 486px 490px,#fafafa 490px)}
.collage{position:absolute;top:0;left:0;width:360px;height:290px}
.cover__brand{position:absolute;top:325px;left:0;right:0;text-align:center;color:var(--white)}
.cover .brand-name{font-size:52px;letter-spacing:2px}
.cover .brand-sub{font-size:12.5px;letter-spacing:1px;margin-top:2px}
.cover__url{position:absolute;top:456px;right:104px;color:var(--white);font-size:7.5px;letter-spacing:3.6px}

/* Inside */
.inside{background:linear-gradient(160deg,#f8f8f8,#e9e9e9)}
.page-head{position:absolute;top:0;left:0;right:0;height:44px;background:var(--wine);border-bottom:2px solid #a8a8a8;color:var(--white)}
.page-head .brand-name{position:absolute;top:13px;font-size:15px}
.page-head .brand-sub{position:absolute;top:28px;font-size:3.6px}
.page-head h2{position:absolute;top:14px;font-family:"Montserrat",sans-serif;font-weight:700;font-size:14px;line-height:17px;letter-spacing:.2px;white-space:nowrap}
.inside--left .page-head .brand-name{left:20px}
.inside--left .page-head .brand-sub{left:32px}
.inside--left .page-head h2{left:162px}
.inside--right .page-head .brand-name{right:22px}
.inside--right .page-head .brand-sub{right:29px}
.inside--right .page-head h2{left:18px}
.games{position:absolute;top:64px;display:grid;grid-template-columns:170px 170px;grid-auto-rows:78px;row-gap:15px}
.inside--left .games{left:19px}
.inside--right .games{left:18px}
.game{position:relative}
.game__thumb{position:absolute;left:0;top:0;width:60px;height:78px;border:1px solid #ddd}
.game__info{position:absolute;left:59px;top:7px;width:91px;height:63px;background:var(--white);border:1px solid #c8c8c8;border-left:none;padding:5px 0 0 8px;font-family:"Roboto",sans-serif;font-size:6.6px;line-height:10.5px;color:#222;white-space:nowrap}
.game__info h3{font-size:6.8px;font-weight:700;color:var(--wine)}
.game__info b{font-weight:700}
.notes{position:absolute;top:455px;left:19px;font-size:5.2px;line-height:9.8px;color:#444;white-space:nowrap}
.page-foot{position:absolute;top:488px;font-size:6.6px;letter-spacing:.8px;color:#444}
.inside--left .page-foot{left:19px}
.inside--right .page-foot{right:20px}
.foot-rule{position:absolute;top:492px;height:1px;background:var(--wine)}
.inside--left .foot-rule{left:115px;right:0}
.inside--right .foot-rule{left:0;right:113px}
</style>
</head>
<body>

<section class="spread spread--outside">
  <div class="page back">
    <div class="back__intro">
      <span class="quote-rule quote-rule--l"></span>
      <span class="quote-rule quote-rule--r"></span>
      <div class="quote-mark">&ldquo;</div>
      <div class="intro-text">
        <p>Corvane Events Pte Ltd is your preferred event management that specializes in offering customized solutions irrespective of size or budget.</p>
        <p class="justify">With more than a decade of experience, we have managed outdoors and indoor events of all scale types. This includes movie screenings, product launches, large-scale seminars for corporate clients, planned training and consultancy deep-dive sessions for mid-sized companies and private events for individuals.</p>
        <p>We are a partner of SKYFRAME and also an official Velvet Hall Booking Agent.</p>
      </div>
    </div>
    <div class="back__contact">
      <div class="brand-name">CORVANE</div>
      <div class="brand-sub">CORVANE EVENTS PTE LTD</div>
      <div class="contact-icons">
        <svg viewBox="0 0 16 16" aria-hidden="true"><circle cx="8" cy="8" r="7.3" fill="none" stroke="#fff" stroke-width="1"/><path d="M8 3.6a2.6 2.6 0 0 0-2.6 2.6C5.4 8.2 8 11.8 8 11.8s2.6-3.6 2.6-5.6A2.6 2.6 0 0 0 8 3.6z" fill="#fff"/><circle cx="8" cy="6.2" r="1" fill="var(--wine)"/></svg>
        <svg viewBox="0 0 16 16" aria-hidden="true"><circle cx="8" cy="8" r="7.3" fill="none" stroke="#fff" stroke-width="1"/><rect x="4" y="5.2" width="8" height="5.6" fill="#fff"/><path d="M4 5.4l4 3 4-3" fill="none" stroke="var(--wine)" stroke-width=".8"/></svg>
        <svg viewBox="0 0 16 16" aria-hidden="true"><circle cx="8" cy="8" r="7.3" fill="none" stroke="#fff" stroke-width="1"/><circle cx="8" cy="8" r="4" fill="none" stroke="#fff" stroke-width=".8"/><ellipse cx="8" cy="8" rx="1.7" ry="4" fill="none" stroke="#fff" stroke-width=".8"/><path d="M4 8h8M4.6 6h6.8M4.6 10h6.8" stroke="#fff" stroke-width=".6"/></svg>
      </div>
      <p class="address">18 Harbour Lane, Meridian Building,<br>#05-12, Singapore 100218</p>
      <p class="web">hello@corvane.com.sg<br>www.corvane.com.sg</p>
      <p class="tagline">A Definite Answer to Your Needs</p>
      <p class="social"><span class="dot"></span>social.corvane.com.sg/events</p>
    </div>
  </div>

  <div class="page cover">
    <svg class="collage" viewBox="0 0 360 290" role="img" aria-label="Collage of event photographs in diamond frames: lion dance performers, a stage booth, guests at a corporate event, fireworks, children at a craft table and an inflatable game">
      <defs>
        <linearGradient id="g-lion" x1="0" y1="0" x2="1" y2="1"><stop offset="0" stop-color="#d9d0c8"/><stop offset="1" stop-color="#b8202c"/></linearGradient>
        <linearGradient id="g-stage" x1="0" y1="0" x2="0" y2="1"><stop offset="0" stop-color="#f2a4b8"/><stop offset="1" stop-color="#c2475f"/></linearGradient>
        <linearGradient id="g-guests" x1="0" y1="0" x2="1" y2="1"><stop offset="0" stop-color="#a9b6bd"/><stop offset="1" stop-color="#3c4552"/></linearGradient>
        <linearGradient id="g-fire" x1="0" y1="0" x2="0" y2="1"><stop offset="0" stop-color="#2a0c12"/><stop offset="1" stop-color="#8a3b3b"/></linearGradient>
        <linearGradient id="g-kids" x1="0" y1="0" x2="1" y2="1"><stop offset="0" stop-color="#8c7d73"/><stop offset="1" stop-color="#e8e2a0"/></linearGradient>
        <linearGradient id="g-game" x1="0" y1="0" x2="1" y2="1"><stop offset="0" stop-color="#d8d8e0"/><stop offset="1" stop-color="#d42a2a"/></linearGradient>
      </defs>
      <g stroke="#fff" stroke-width="4">
        <polygon points="60,-65 175,50 60,165 -55,50" fill="url(#g-lion)"/>
        <polygon points="180,-40 228,8 180,56 132,8" fill="url(#g-stage)"/>
        <polygon points="300,-70 400,30 300,130 200,30" fill="url(#g-guests)"/>
        <polygon points="35,108 120,193 35,278 -50,193" fill="url(#g-fire)"/>
        <polygon points="345,140 410,205 345,270 280,205" fill="url(#g-game)"/>
        <polygon points="180,75 290,185 180,295 70,185" fill="url(#g-kids)"/>
      </g>
    </svg>
    <div class="cover__brand">
      <div class="brand-name">CORVANE</div>
      <div class="brand-sub">CORVANE EVENTS PTE LTD</div>
    </div>
    <div class="cover__url">www.corvane.com.sg</div>
  </div>
</section>

<section class="spread spread--inside">
  <div class="page inside inside--left">
    <header class="page-head">
      <div class="brand-name">CORVANE</div>
      <div class="brand-sub">CORVANE EVENTS PTE LTD</div>
      <h2>CARNIVAL GAME STALLS</h2>
    </header>
    <div class="games">
      <article class="game"><div class="game__thumb" role="img" aria-label="Carnival ring toss stall with pegs and rings" style="background:linear-gradient(180deg,#e9e6e0,#c0504d 60%,#2a2a2a)"></div><div class="game__info"><h3>Carnival Ring Toss</h3>0.93m by 0.93m<br>$145/stall (Min 3 stalls)<br>Require 1x Table<br>Subsequent day: <b>$70</b></div></article>
      <article class="game"><div class="game__thumb" role="img" aria-label="Milk cans toss stall with stacked cans" style="background:linear-gradient(160deg,#f5d23b,#e8e8e8 55%,#8a8a8a)"></div><div class="game__info"><h3>Milk Cans Toss</h3>0.93m by 0.93m<br>$145/stall (Min 3 stalls)<br>Require 1x Table<br>Subsequent day: <b>$70</b></div></article>
      <article class="game"><div class="game__thumb" role="img" aria-label="Match the colour stall with coloured grid" style="background:linear-gradient(180deg,#2a2a2a,#d9463a 55%,#3a7fd0)"></div><div class="game__info"><h3>Match The Colour</h3>0.93m by 0.93m<br>$145/stall (Min 3 stalls)<br>Require 1x Table<br>Subsequent day: <b>$70</b></div></article>
      <article class="game"><div class="game__thumb" role="img" aria-label="Feed the clown stall board" style="background:linear-gradient(180deg,#f5a623,#f3f3f3 70%,#d94c4c)"></div><div class="game__info"><h3>Feed The Clown</h3>0.93m by 0.93m<br>$145/stall (Min 3 stalls)<br>Require 1x Table<br>Subsequent day: <b>$70</b></div></article>
      <article class="game"><div class="game__thumb" role="img" aria-label="Feed the bear stall board on brick backdrop" style="background:linear-gradient(180deg,#c8a070,#c2573c)"></div><div class="game__info"><h3>Feed The Bear</h3>0.93m by 0.93m<br>$145/stall (Min 3 stalls)<br>Require 1x Table<br>Subsequent day: <b>$70</b></div></article>
      <article class="game"><div class="game__thumb" role="img" aria-label="Feed the pig stall board" style="background:linear-gradient(180deg,#7cc86a,#f19aa6 55%,#e7d7a0)"></div><div class="game__info"><h3>Feed The Pig</h3>0.93m by 0.93m<br>$145/stall (Min 3 stalls)<br>Require 1x Table<br>Subsequent day: <b>$70</b></div></article>
      <article class="game"><div class="game__thumb" role="img" aria-label="Shoot the duck stall with red frame" style="background:linear-gradient(180deg,#3a8fd0,#e4c45a 50%,#5bc0de)"></div><div class="game__info"><h3>Shoot The Duck</h3>0.93m by 0.93m<br>$145/stall (Min 3 stalls)<br>Require 1x Table<br>Subsequent day: <b>$70</b></div></article>
      <article class="game"><div class="game__thumb" role="img" aria-label="Shoot the alien stall with red frame" style="background:linear-gradient(180deg,#2c3e5a,#7a8a6a 55%,#d8d8d8)"></div><div class="game__info"><h3>Shoot The Alien</h3>0.93m by 0.93m<br>$145/stall (Min 3 stalls)<br>Require 1x Table<br>Subsequent day: <b>$70</b></div></article>
    </div>
    <div class="notes">*Size stated above is estimated only.<br>*Rates include Delivery, Set up, Dismantle and Collection of the equipments.<br>*The more items or more days rented, we may be able to quote a much better discounted package rate.</div>
    <div class="page-foot">www.corvane.com.sg</div>
    <span class="foot-rule"></span>
  </div>

  <div class="page inside inside--right">
    <header class="page-head">
      <h2>CARNIVAL GAME STALLS</h2>
      <div class="brand-name">CORVANE</div>
      <div class="brand-sub">CORVANE EVENTS PTE LTD</div>
    </header>
    <div class="games">
      <article class="game"><div class="game__thumb" role="img" aria-label="Shoot the target stall with red frame" style="background:linear-gradient(180deg,#e6e6e6,#5aa04a 60%,#f0f0f0)"></div><div class="game__info"><h3>Shoot The Target</h3>0.93m by 0.93m<br>$145/stall (Min 3 stalls)<br>Require 1x Table<br>Subsequent day: <b>$70</b></div></article>
      <article class="game"><div class="game__thumb" role="img" aria-label="Finish the race stall with racing lanes" style="background:linear-gradient(180deg,#1c1c1c,#2b3a4a 60%,#1c1c1c)"></div><div class="game__info"><h3>Finish The Race</h3>0.93m by 0.93m<br>$145/stall (Min 3 stalls)<br>Require 1x Table<br>Subsequent day: <b>$70</b></div></article>
      <article class="game"><div class="game__thumb" role="img" aria-label="Archery game stall with target board" style="background:linear-gradient(180deg,#d9683a,#c85a30 65%,#3a9a6a)"></div><div class="game__info"><h3>Archery Game</h3>0.93m by 0.93m<br>$145/stall (Min 3 stalls)<br>Require 1x Table<br>Subsequent day: <b>$70</b></div></article>
      <article class="game"><div class="game__thumb" role="img" aria-label="Dart game stall with dartboard" style="background:linear-gradient(180deg,#1f3f8a,#1f3f8a 70%,#e8402a)"></div><div class="game__info"><h3>Dart Game</h3>0.93m by 0.93m<br>$145/stall (Min 3 stalls)<br>Require 1x Table<br>Subsequent day: <b>$70</b></div></article>
      <article class="game"><div class="game__thumb" role="img" aria-label="Basketball game stall with hoop" style="background:linear-gradient(180deg,#f0501e,#e6401a)"></div><div class="game__info"><h3>Basketball Game</h3>0.93m by 0.93m<br>$145/stall (Min 3 stalls)<br>Require 1x Table<br>Subsequent day: <b>$70</b></div></article>
      <article class="game"><div class="game__thumb" role="img" aria-label="Fetch game stall with beach scene" style="background:linear-gradient(180deg,#7fc4ea,#f1e7c9 70%,#dfe8ee)"></div><div class="game__info"><h3>Fetch Game</h3>0.93m by 0.93m<br>$145/stall (Min 3 stalls)<br>Require 1x Table<br>Subsequent day: <b>$70</b></div></article>
      <article class="game"><div class="game__thumb" role="img" aria-label="Coin toss stall with coin board" style="background:linear-gradient(180deg,#2a86d6,#f3c93a 45%,#1fa0d8)"></div><div class="game__info"><h3>Coin Toss</h3>0.93m by 0.93m<br>$145/stall (Min 3 stalls)<br>Require 1x Table<br>Subsequent day: <b>$70</b></div></article>
      <article class="game"><div class="game__thumb" role="img" aria-label="Tic tac toe stall board" style="background:linear-gradient(180deg,#2f5fbf,#3a8a4a 60%,#e04030)"></div><div class="game__info"><h3>Tic Tac Toe</h3>0.93m by 0.93m<br>$145/stall (Min 3 stalls)<br>Require 1x Table<br>Subsequent day: <b>$70</b></div></article>
    </div>
    <div class="notes">*Size stated above is estimated only.<br>*Rates include Delivery, Set up, Dismantle and Collection of the equipments.<br>*The more items or more days rented, we may be able to quote a much better discounted package rate.</div>
    <span class="foot-rule"></span>
    <div class="page-foot">www.corvane.com.sg</div>
  </div>
</section>

</body>
</html>
```